Road Keeper Community Awareness Poster

We are looking for a tabloid size (11"x17") Poster to be placed all over various towns and communities promoting our business. We need something that grabs the attention of our target demographic (parents of teen drivers) and gets them to want to learn more about our programs and ultimately sign up for one of our events.

see our website for more information at www.roadkeeperhub.example

Target Market(s)

We want parents of teens ages 15 - 19 to be aware how dangerous driving is for new drivers and compel them to sign their teen up for our program.

Industry/Entity Type

Community

Requirements
Must have
• Must have our logo and identity, url and be 11"x17"

```html
<!DOCTYPE html>
<html lang="en">
<head>
<meta charset="utf-8">
<title>Road Keeper – Community Awareness Poster</title>
<link rel="stylesheet" href="https://fonts.googleapis.com/css2?family=PT+Sans:wght@400;700&display=swap">
<style>
  :root {
    --ink: #000000;
    --green: #4ca83c;
    --white: #ffffff;
  }
  html, body {
    margin: 0;
    padding: 0;
    width: 789px;
    height: 1200px;
    overflow: hidden;
    background: var(--ink);
  }
  .poster {
    position: relative;
    width: 789px;
    height: 1200px;
    background: var(--ink);
    font-family: "PT Sans", "Myriad Pro", sans-serif;
    color: var(--green);
    overflow: hidden;
  }
  .monologue {
    position: absolute;
    left: 78px;
    top: 80px;
    margin: 0;
    font-size: 34px;
    line-height: 47.4px;
    font-weight: 400;
    white-space: nowrap;
    color: var(--green);
  }
  .monologue .lift { position: relative; top: -7px; font-size: 28px; }
  .spill {
    position: absolute;
    inset: 0;
    pointer-events: none;
  }
  .spill span {
    position: absolute;
    display: block;
    color: var(--green);
    font-size: 24px;
    line-height: 1;
    transform-origin: left center;
    white-space: nowrap;
  }
  .headline {
    position: absolute;
    left: 79px;
    top: 855px;
    margin: 0;
    font-size: 29px;
    line-height: 45.5px;
    font-weight: 400;
    white-space: nowrap;
    color: var(--white);
  }
  .cta {
    position: absolute;
    left: 79px;
    top: 1027px;
    margin: 0;
    font-size: 17.5px;
    line-height: 27px;
    white-space: nowrap;
    color: var(--green);
  }
  .url {
    position: absolute;
    left: 79px;
    top: 1090px;
    margin: 0;
    font-size: 18.5px;
    line-height: 24px;
    color: var(--white);
  }
  .brand {
    position: absolute;
    left: 490px;
    top: 948px;
    width: 200px;
    text-align: center;
  }
  .brand-mark {
    display: block;
    margin: 0 auto;
  }
  .brand-name {
    display: block;
    margin-top: 10px;
    font-size: 26px;
    line-height: 30px;
    font-weight: 700;
    letter-spacing: 0.3px;
    white-space: nowrap;
    color: var(--white);
  }
</style>
</head>
<body>
<main class="poster">
  <p class="monologue">So then I told Ashley I wasn’t<br>into him, and if she liked him,<br>go for it. I think he’s going to<br>ask her to prom. I really wish<br>Jason would ask me, but I<br>think he’s just been really<br>busy with basketball and<br>stuff, and my parents totally<br>won’t pay for the dress I want<br>because I failed my m<span class="lift">at</span>h te</p>

  <div class="spill" aria-label="the sentence trails off and tumbles down the page">
    <span style="left:530px;top:510px;font-size:27px;">s</span>
    <span style="left:548px;top:530px;transform:rotate(62deg);">t</span>
    <span style="left:552px;top:548px;transform:rotate(50deg);">totally</span>
    <span style="left:582px;top:618px;transform:rotate(18deg);font-size:26px;">and</span>
    <span style="left:545px;top:656px;transform:rotate(12deg);font-size:25px;">now</span>
    <span style="left:584px;top:673px;transform:rotate(28deg);font-size:18px;">they</span>
    <span style="left:630px;top:712px;font-size:26px;">g</span>
    <span style="left:552px;top:741px;transform:rotate(20deg);font-size:25px;">b</span>
    <span style="left:600px;top:745px;transform:rotate(-22deg);font-size:22px;">ein</span>
    <span style="left:578px;top:764px;transform:rotate(-30deg);font-size:22px;">your</span>
    <span style="left:618px;top:768px;transform:rotate(-14deg);font-size:24px;">are</span>
    <span style="left:521px;top:792px;transform:rotate(-48deg);font-size:26px;">you</span>
    <span style="left:546px;top:786px;font-size:24px;">future</span>
    <span style="left:558px;top:780px;transform:rotate(8deg);font-size:26px;">ruin</span>
    <span style="left:610px;top:788px;font-size:26px;">fun</span>
    <span style="left:530px;top:802px;transform:rotate(10deg);font-size:24px;">jmfor</span>
    <span style="left:596px;top:805px;font-size:22px;">r</span>
    <span style="left:636px;top:805px;font-size:22px;">r</span>
  </div>

  <h1 class="headline">Think your problems seem big<br>now? If you don’t pay attention<br>on the road, they could<br>become even bigger.</h1>

  <p class="cta">Visit our website to sign up for a life-saving<br>course that’s only half a day.</p>

  <p class="url">www.roadkeeperhub.example</p>

  <div class="brand">
    <svg class="brand-mark" width="122" height="122" viewBox="0 0 122 122" aria-hidden="true">
      <circle cx="61" cy="61" r="60" fill="var(--white)"/>
    </svg>
    <span class="brand-name">ROAD KEEPER</span>
  </div>
</main>
</body>
</html>
```